Business Card Design Project

I am a consultant mostly to mining or large infrastructure companies - so a little conservative. I am looking for a business card with a logo. I will then put the logo in my signature page for emails etc also.

The company is called Tolvenna Capital and comprises Tolvenna Offshore Pte Ltd based in SIngapore and Tolvenna Consulting Pty Ltd based in Australia.

Tolvena is a beach in Byron Bay Australia. It has a large lighthouse above it which I would like included in the design. Beaches etc are not very professional or conservative but i think we could work the lighthouse in.

Here it is http://en.plorvexa.org/wiki/Morrow_Head_Beacon

I will not have address details but will have 2x phones and 1 skype and 1x email address

Conservative

```html
<!DOCTYPE html>
<html lang="en">
<head>
<meta charset="utf-8">
<title>Tolvenna Capital — Business Card</title>
<link rel="stylesheet" href="https://fonts.googleapis.com/css2?family=Questrial&display=swap">
<style>
  :root {
    --navy-deep: #0f1c3d;
    --navy: #17295a;
    --navy-glow: #34548f;
    --paper: #f7f8fa;
    --paper-shade: #e4e7ec;
    --rule-light: rgba(255,255,255,0.55);
    --rule-dark: #2a3a66;
    --text-light: #e6eaf3;
    --text-muted: #b9c3da;
    --backdrop: #e9e9ec;
  }
  * { margin: 0; padding: 0; box-sizing: border-box; }
  html, body {
    width: 1200px; height: 900px; overflow: hidden;
    background: var(--backdrop);
    font-family: "Questrial", "Century Gothic", sans-serif;
  }
  .canvas {
    position: relative; width: 1200px; height: 900px;
  }
  .card {
    position: absolute; left: 250px;
    width: 700px; height: 400px;
    overflow: hidden;
    box-shadow: 0 6px 18px rgba(0,0,0,0.18);
  }
  .card--front {
    top: 34px;
    background: radial-gradient(ellipse 55% 65% at 50% 42%, var(--navy-glow) 0%, var(--navy) 55%, var(--navy-deep) 100%);
  }
  .card--back {
    top: 466px;
    background: var(--navy);
  }
  .rule { position: absolute; height: 1px; }
  .card--front .rule { background: var(--rule-light); }
  .card--front .rule--left { left: 90px; top: 300px; width: 165px; }
  .card--front .rule--right { right: 90px; top: 138px; width: 165px; }

  .brand {
    position: absolute; display: flex; align-items: center; gap: 12px;
    left: 50%; transform: translateX(-50%);
    white-space: nowrap;
  }
  .brand__mark { width: 18px; height: 18px; }
  .brand__name { font-size: 30px; letter-spacing: 0.5px; }
  .card--front .brand { top: 200px; color: var(--text-light); }
  .card--front .brand__mark { background: var(--text-light); }

  .band {
    position: absolute; left: 0; top: 0; width: 100%; height: 215px;
    background: linear-gradient(180deg, #ffffff 0%, var(--paper) 70%, var(--paper-shade) 100%);
  }
  .card--back .brand { top: 62px; color: var(--navy); }
  .card--back .brand__name { font-size: 24px; }
  .card--back .brand__mark { width: 14px; height: 14px; background: var(--navy); }
  .band .rule { background: var(--rule-dark); }
  .band .rule--left { left: 150px; top: 146px; width: 130px; }
  .band .rule--right { right: 110px; top: 92px; width: 110px; }

  .person {
    position: absolute; left: 0; width: 100%; top: 166px; text-align: center;
    color: var(--navy);
  }
  .person__name { font-size: 20px; letter-spacing: 0.5px; }
  .person__role { font-size: 11px; letter-spacing: 0.4px; color: #4a5a80; }

  .contact {
    position: absolute;
    border-left: 1px solid var(--rule-light);
    padding-left: 26px;
    display: flex; flex-direction: column; gap: 16px;
    color: var(--text-muted); font-size: 12px; letter-spacing: 0.8px;
  }
  .contact--phones { left: 90px; top: 295px; height: 80px; justify-content: center; }
  .contact--online { right: 80px; top: 232px; height: 66px; justify-content: center; }
  .contact__line { display: flex; align-items: center; gap: 22px; }
  .contact__icon { width: 12px; height: 12px; flex: none; color: var(--text-muted); }
  .contact__dot { width: 11px; height: 11px; border-radius: 50%; background: var(--text-muted); flex: none; }
  .contact__at { width: 12px; font-size: 13px; text-align: center; flex: none; }
</style>
</head>
<body>
<main class="canvas">

  <section class="card card--front" aria-label="Card front">
    <div class="rule rule--right"></div>
    <div class="brand">
      <span class="brand__mark"></span>
      <span class="brand__name">Tolvenna Capital</span>
    </div>
    <div class="rule rule--left"></div>
  </section>

  <section class="card card--back" aria-label="Card back">
    <div class="band">
      <div class="rule rule--right"></div>
      <div class="brand">
        <span class="brand__mark"></span>
        <span class="brand__name">Tolvenna Capital</span>
      </div>
      <div class="rule rule--left"></div>
      <div class="person">
        <div class="person__name">Daniel Harrow</div>
        <div class="person__role">general manager</div>
      </div>
    </div>

    <div class="contact contact--online">
      <div class="contact__line">
        <span class="contact__dot"></span>
        <span>d.harrow.tolvenna</span>
      </div>
      <div class="contact__line">
        <span class="contact__at">@</span>
        <span>harrow@tolvenna.com</span>
      </div>
    </div>

    <div class="contact contact--phones">
      <div class="contact__line">
        <svg class="contact__icon" viewBox="0 0 12 12" aria-hidden="true">
          <rect x="3" y="0.5" width="6" height="11" rx="1" fill="none" stroke="currentColor" stroke-width="1"/>
          <line x1="5" y1="10" x2="7" y2="10" stroke="currentColor" stroke-width="0.8"/>
        </svg>
        <span>000 481 902 377</span>
      </div>
      <div class="contact__line">
        <svg class="contact__icon" viewBox="0 0 12 12" aria-hidden="true">
          <path d="M3 1.2 L4.6 3.6 L3.6 4.8 C4.3 6.3 5.6 7.6 7.2 8.4 L8.4 7.4 L10.8 9 L9.8 10.8 C5.6 10.6 1.4 6.4 1.2 2.2 Z" fill="none" stroke="currentColor" stroke-width="1"/>
        </svg>
        <span>0133 604 218</span>
      </div>
    </div>
  </section>

</main>
</body>
</html>
```